Marlow Hire Business Card for recruitment company

We are looking for a Business Card Design that incorporates our personal details and our busines name and logo. We are a specialized search consultancy that recruit Property and Construction professionals.
We would like a business card that stands out and is appealing to the Construction and Property industry as well.

Target Market(s)

people in the construction and property industry

Contact Information for Business Card

Business Name and logo

Font styles to use
Serif

Colors
0094D4
00A9DD
6FCCEA
C7EBF8
E9F6FB

Requirements
Must have
• Business name and logo as well as contact details
Should not have
• No photos of us please

```html
<!DOCTYPE html>
<html lang="en">
<head>
<meta charset="utf-8">
<title>Marlow Hire – Business Card</title>
<link rel="stylesheet" href="https://fonts.googleapis.com/css2?family=Josefin+Sans:wght@300&family=Montserrat:wght@400;500&display=swap">
<style>
  :root {
    --card-navy: #033d52;
    --card-ink: #ffffff;
    --page-bg: #ecebe8;
  }
  * { box-sizing: border-box; margin: 0; padding: 0; }
  html, body { width: 1200px; height: 900px; overflow: hidden; }
  body { background: var(--page-bg); position: relative; font-family: "Montserrat", sans-serif; color: var(--card-ink); }

  .card {
    position: absolute;
    left: 261px;
    width: 656px;
    height: 357px;
    background: var(--card-navy);
    border-radius: 20px;
    overflow: hidden;
  }
  .card--front { top: 69px; }
  .card--back { top: 472px; }

  .wordmark {
    position: absolute;
    font-family: "Josefin Sans", sans-serif;
    font-weight: 300;
    letter-spacing: 0.02em;
    white-space: nowrap;
    line-height: 1;
    color: var(--card-ink);
  }
  .card--front .wordmark { left: 34px; top: 40px; font-size: 40px; }
  .card--back .wordmark { left: 0; right: 0; top: 152px; text-align: center; font-size: 62px; }

  .brand-badge {
    position: absolute;
    left: 301px;
    top: 36px;
    width: 330px;
    height: 330px;
    border-radius: 50%;
    background: var(--card-ink);
    display: flex;
    align-items: center;
    justify-content: center;
  }
  .brand-badge__name {
    font-family: "Josefin Sans", sans-serif;
    font-weight: 300;
    font-size: 36px;
    letter-spacing: 0.02em;
    line-height: 1;
    white-space: nowrap;
    color: var(--card-navy);
  }

  .holder { position: absolute; left: 34px; top: 180px; }
  .holder__name { font-size: 27px; font-weight: 500; letter-spacing: 0.03em; line-height: 1; }
  .holder__role { font-size: 16px; font-weight: 400; letter-spacing: 0.05em; margin-top: 5px; }

  .contact-list { position: absolute; left: 33px; top: 240px; list-style: none; }
  .contact-list__item {
    display: flex; align-items: center; gap: 6px;
    font-size: 17px; letter-spacing: 0.03em; line-height: 21px;
  }
  .contact-list__icon { width: 12px; height: 12px; flex: none; }
</style>
</head>
<body>
  <section class="card card--front">
    <div class="wordmark">MARLOW HIRE</div>

    <div class="brand-badge">
      <span class="brand-badge__name">MARLOW HIRE</span>
    </div>

    <div class="holder">
      <div class="holder__name">DECLAN ROSS</div>
      <div class="holder__role">FOUNDER</div>
    </div>

    <ul class="contact-list">
      <li class="contact-list__item">
        <svg class="contact-list__icon" viewBox="0 0 12 12" aria-hidden="true"><path d="M3 1 L5 3.5 L4 5 Q5 7.5 7 8 L8.5 7 L11 9 L9.5 11 Q3 10 1 2.5 Z" fill="none" stroke="#fff" stroke-width="1"/></svg>
        +64 21 555 0183
      </li>
      <li class="contact-list__item">
        <svg class="contact-list__icon" viewBox="0 0 12 12" aria-hidden="true"><rect x="1" y="2.5" width="10" height="7" fill="none" stroke="#fff" stroke-width="1"/><path d="M1 2.5 L6 6.5 L11 2.5" fill="none" stroke="#fff" stroke-width="1"/></svg>
        declan@marlowhire.co
      </li>
      <li class="contact-list__item">
        <svg class="contact-list__icon" viewBox="0 0 12 12" aria-hidden="true"><circle cx="6" cy="6" r="5" fill="none" stroke="#fff" stroke-width="0.9"/><ellipse cx="6" cy="6" rx="2.2" ry="5" fill="none" stroke="#fff" stroke-width="0.8"/><path d="M1 6 H11 M2 3.5 H10 M2 8.5 H10" stroke="#fff" stroke-width="0.8"/></svg>
        www.marlowhire.co
      </li>
      <li class="contact-list__item">
        <svg class="contact-list__icon" viewBox="0 0 12 12" aria-hidden="true"><path d="M6 11.5 L2.6 6 A3.8 3.8 0 1 1 9.4 6 Z" fill="#fff"/><circle cx="6" cy="4.3" r="1.3" fill="#033d52"/></svg>
        Kestrel Bay, New Zealand
      </li>
    </ul>
  </section>

  <section class="card card--back">
    <div class="wordmark">MARLOW HIRE</div>
  </section>
</body>
</html>
```